merin grains company small package

we are looking to design a package for our nuts 10cm by 13 cm and also 3.25 inch by 4.5 inches. our nuts are:
Salted peanuts
honey roasted peanuts
salted cashews
honey roasted cashews
pistachios
sunflower seeds

have a floral design simple yet elegant not too crowded
our product is non GMO

some of our competitors:
http://velkaseed.ae/
http://www.duneharvest.com/sg/
http://tobrik.net/en/content/view/5/17/

Target Market(s)

european market, Middle eastern market

Industry/Entity Type

It Company

Font styles to use
Decorative
Script

Requirements
Must have
• floral design not crowded yet elegant
• high resolution pictures of the nuts
Nice to have
Should not have
• cartoon characters

```html
<!DOCTYPE html>
<html lang="en">
<head>
<meta charset="utf-8">
<title>Merin Grains – Peanut Packages</title>
<link rel="stylesheet" href="https://fonts.googleapis.com/css2?family=Great+Vibes&family=Oswald:wght@600&family=Libre+Baskerville&display=swap">
<style>
  :root {
    --stage: #3a3a3a;
    --pack-black: #0d0d0d;
    --pattern-dark: #1c1c1c;
    --pattern-mid: #2a2a2a;
    --ink: #1a1a1a;
    --brand-white: #ffffff;
    --silver-dark: #bdbdbd;
    --silver-light: #ffffff;
    --gold-dark: #b38a25;
    --gold-light: #f6e493;
    --peanut-light: #e9b46a;
    --peanut-dark: #b8742e;
    --honey-light: #d08a3c;
    --honey-dark: #8e4f1c;
  }
  html, body {
    margin: 0;
    width: 1200px;
    height: 1120px;
    overflow: hidden;
    background: var(--stage);
  }
  .canvas {
    position: relative;
    width: 1200px;
    height: 1120px;
  }
  .pack {
    position: absolute;
    top: 110px;
    width: 507px;
    height: 660px;
  }
  .pack--salted { left: 48px; }
  .pack--honey { left: 638px; }
  .pack svg { display: block; }
  .brand-name {
    font-family: "Oswald", sans-serif;
    font-weight: 600;
    font-size: 58px;
    fill: var(--brand-white);
    letter-spacing: 1px;
  }
  .flavour-title {
    font-family: "Great Vibes", cursive;
    font-size: 66px;
    fill: var(--ink);
  }
  .pack--honey .flavour-title { font-size: 56px; }
  .pack-note {
    font-family: "Libre Baskerville", serif;
    font-size: 15px;
    fill: var(--ink);
  }
</style>
</head>
<body>
<main class="canvas">

  <section class="pack pack--salted">
    <svg width="507" height="660" viewBox="0 0 507 660">
      <defs>
        <linearGradient id="silver-band" x1="0" y1="0" x2="1" y2="0">
          <stop offset="0" stop-color="var(--silver-dark)"/>
          <stop offset="0.45" stop-color="var(--silver-light)"/>
          <stop offset="1" stop-color="var(--silver-dark)"/>
        </linearGradient>
        <radialGradient id="peanut-fill" cx="0.5" cy="0.5" r="0.7">
          <stop offset="0" stop-color="var(--peanut-light)"/>
          <stop offset="1" stop-color="var(--peanut-dark)"/>
        </radialGradient>
        <linearGradient id="damask-fill-s" x1="0" y1="0" x2="1" y2="1">
          <stop offset="0" stop-color="var(--pattern-mid)"/>
          <stop offset="1" stop-color="var(--pattern-dark)"/>
        </linearGradient>
      </defs>
      <rect class="pack-body" width="507" height="660" fill="var(--pack-black)"/>
      <rect class="floral-pattern" width="507" height="230" fill="url(#damask-fill-s)" role="img" aria-label="Subtle dark floral damask pattern"/>
      <g class="brand-mark">
        <text class="brand-name" x="253" y="137" text-anchor="middle">MERIN</text>
      </g>
      <rect class="product-photo" y="330" width="507" height="280" fill="url(#peanut-fill)" role="img" aria-label="Close-up photo of salted roasted peanuts"/>
      <path class="band-swoosh" d="M40 212 Q253 180 467 212" fill="none" stroke="url(#silver-band)" stroke-width="5"/>
      <path class="title-band" d="M0 205 Q120 205 200 225 Q253 240 306 225 Q387 205 507 205 L507 370 Q400 360 330 350 Q290 345 270 352 Q253 358 236 352 Q216 345 176 350 Q106 360 0 370 Z" fill="url(#silver-band)" stroke="var(--ink)" stroke-width="2"/>
      <text class="flavour-title" x="253" y="318" text-anchor="middle">Salted Peanuts</text>
      <path class="footer-band" d="M0 582 Q106 588 180 590 Q225 592 240 605 Q253 614 266 605 Q281 592 326 590 Q400 588 507 582 L507 660 L0 660 Z" fill="url(#silver-band)" stroke="var(--ink)" stroke-width="2"/>
      <text class="pack-note" x="14" y="641">non GMO</text>
      <text class="pack-note" x="398" y="641">Cont:</text>
    </svg>
  </section>

  <section class="pack pack--honey">
    <svg width="507" height="660" viewBox="0 0 507 660">
      <defs>
        <linearGradient id="gold-band" x1="0" y1="0" x2="1" y2="0">
          <stop offset="0" stop-color="var(--gold-dark)"/>
          <stop offset="0.45" stop-color="var(--gold-light)"/>
          <stop offset="1" stop-color="var(--gold-dark)"/>
        </linearGradient>
        <radialGradient id="honey-fill" cx="0.5" cy="0.5" r="0.7">
          <stop offset="0" stop-color="var(--honey-light)"/>
          <stop offset="1" stop-color="var(--honey-dark)"/>
        </radialGradient>
        <linearGradient id="damask-fill-h" x1="0" y1="0" x2="1" y2="1">
          <stop offset="0" stop-color="var(--pattern-mid)"/>
          <stop offset="1" stop-color="var(--pattern-dark)"/>
        </linearGradient>
      </defs>
      <rect class="pack-body" width="507" height="660" fill="var(--pack-black)"/>
      <rect class="floral-pattern" width="507" height="230" fill="url(#damask-fill-h)" role="img" aria-label="Subtle dark floral damask pattern"/>
      <g class="brand-mark">
        <text class="brand-name" x="253" y="137" text-anchor="middle">MERIN</text>
      </g>
      <rect class="product-photo" y="330" width="507" height="280" fill="url(#honey-fill)" role="img" aria-label="Close-up photo of honey roasted peanuts"/>
      <path class="band-swoosh" d="M40 212 Q253 180 467 212" fill="none" stroke="url(#gold-band)" stroke-width="5"/>
      <path class="title-band" d="M0 205 Q120 205 200 225 Q253 240 306 225 Q387 205 507 205 L507 370 Q400 360 330 350 Q290 345 270 352 Q253 358 236 352 Q216 345 176 350 Q106 360 0 370 Z" fill="url(#gold-band)" stroke="var(--ink)" stroke-width="2"/>
      <text class="flavour-title" x="253" y="314" text-anchor="middle">Honey Roasted Peanuts</text>
      <path class="footer-band" d="M0 582 Q106 588 180 590 Q225 592 240 605 Q253 614 266 605 Q281 592 326 590 Q400 588 507 582 L507 658 L0 658 Z" fill="url(#gold-band)" stroke="var(--ink)" stroke-width="2"/>
      <text class="pack-note" x="14" y="639">non GMO</text>
      <text class="pack-note" x="400" y="639">Cont:</text>
    </svg>
  </section>

</main>
</body>
</html>
```